Corvell Social "is a company that is focused on managing social media platforms.

I need a website design for a social media management company. The owner is a social media influencer in the Denver, Co area. Would like SG and Tik Tok page intergraded into the site. Would like all post from social to go directly to new website. Also put a page link for blog: her is my blog https://www.plumtrove.com/about

Target Market(s)

Any business that needs social media managed or video made for their company.

Coding

Coded - Design and coding required

Requirements
Must have
• Color scheme needs to match logo ; • SG: https://www.instagram.example/plum.trove/ • ClipTok: https://www.tiktok.example/@plum.trove Please add these videos: https://files.example/b-xQ7mLp2Rta
Nice to have
• • https://greyfinstudio.example/ "this a website that i like in the industry"

```html
<!DOCTYPE html>
<html lang="en">
<head>
<meta charset="utf-8">
<title>Corvell Social — Social Media Management in Denver</title>
<link rel="stylesheet" href="https://fonts.googleapis.com/css2?family=Montserrat:wght@500;600;700;800&family=Lato:wght@400;700&display=swap">
<style>
:root{
  --navy:#0f1c3d;
  --navy-2:#14234a;
  --crimson:#9b1f45;
  --ink:#1d2233;
  --muted:#5b6275;
  --soft:#eef2fb;
  --line:#e6c9d6;
  --white:#ffffff;
  --blue:#3d7fe6;
  --pink:#f07aa5;
  --violet:#8a3cf0;
  --star:#f5b400;
}
*{box-sizing:border-box;margin:0;padding:0}
html,body{width:1200px;height:4228px;overflow:hidden}
body{font-family:'Lato',sans-serif;color:var(--ink);background:var(--white);position:relative}
h1,h2,h3,.heading{font-family:'Montserrat',sans-serif}
.abs{position:absolute}
section{position:absolute;left:0;width:1200px;overflow:hidden}
.btn{position:absolute;display:flex;align-items:center;justify-content:space-between;border-radius:30px;font:700 11px 'Montserrat',sans-serif;padding:0 5px 0 18px}
.btn .arrow{width:26px;height:26px;border-radius:50%;display:flex;align-items:center;justify-content:center}
.btn-dark{background:var(--navy);color:var(--white);border:2px solid var(--navy)}
.btn-dark .arrow{background:var(--white)}
.btn-light{background:var(--white);color:var(--navy)}
.btn-light .arrow{background:var(--navy)}
.brand{display:flex;flex-direction:column;align-items:center;color:var(--white);font:600 11px 'Montserrat',sans-serif;letter-spacing:3px}
.brand .mark{width:40px;height:40px;border:2px solid var(--white);margin-bottom:8px}
.photo{position:absolute}
/* hero */
.hero{top:0;height:640px;background:linear-gradient(100deg,#3f86ee 0%,#6fb6f2 30%,#b6c6f0 52%,#f2a1bd 78%,#f07a9a 100%)}
.nav a{position:absolute;top:40px;font:500 12px 'Montserrat',sans-serif;color:var(--navy);text-decoration:none}
.nav a.active{border-bottom:2px solid var(--navy);font-weight:700}
.pill{border:1.5px solid var(--navy);border-radius:20px;font-size:11px;color:var(--navy);display:flex;align-items:center;justify-content:center}
.hero h1{position:absolute;left:121px;top:222px;font-size:45px;line-height:54px;font-weight:800;color:var(--navy)}
.card{position:absolute;background:var(--white);border-radius:12px;box-shadow:0 8px 22px rgba(20,30,70,.15)}
.checks li{list-style:none;display:flex;align-items:center;gap:8px;font:500 11px 'Montserrat',sans-serif;color:var(--navy);margin-bottom:13px}
.checks .tick{width:12px;height:12px;border-radius:50%;background:var(--blue);display:flex;align-items:center;justify-content:center}
.dot{position:absolute;border-radius:50%}
/* about */
.about{top:640px;height:572px;background:var(--white)}
.label{font-size:11px;color:var(--crimson);display:flex;align-items:center;gap:6px}
.label::after{content:"";width:28px;height:1.5px;background:var(--crimson)}
.label.center::before{content:"";width:28px;height:1.5px;background:var(--crimson)}
.side-word{position:absolute;right:2px;writing-mode:vertical-rl;font:800 64px 'Montserrat',sans-serif;color:#f3e6ec;letter-spacing:4px}
.logo-disc{position:absolute;border-radius:50%;background:var(--navy);border:6px solid var(--white);display:flex;align-items:center;justify-content:center}
/* services */
.services{top:1212px;height:791px;background:var(--soft)}
.svc{position:absolute;width:307px;height:246px;background:var(--white);border:1.5px solid var(--line);text-align:center;padding:0 26px}
.svc .ico{width:50px;height:50px;border-radius:50%;margin:32px auto 18px;background:linear-gradient(135deg,#e7ecfb,#f4dbe9);display:flex;align-items:center;justify-content:center;box-shadow:0 3px 8px rgba(20,30,70,.12)}
.svc .ico span{width:20px;height:20px;border-radius:5px;background:var(--navy)}
.svc h3{font-size:15px;font-weight:600;color:var(--navy);margin-bottom:10px}
.svc p{font-size:10.5px;line-height:18px;color:var(--muted)}
.svc .more{position:absolute;left:0;right:0;bottom:22px;font:700 10px 'Montserrat',sans-serif;color:var(--navy)}
.svc.feature{background:linear-gradient(160deg,#7aa6f2 0%,#c59ef0 45%,#f28bb2 100%);border:none}
.svc.feature h3,.svc.feature p,.svc.feature .more{color:var(--navy)}
/* why */
.why{top:2003px;height:583px;background:var(--white)}
.bullets li{list-style:none;position:absolute;left:121px;font-size:13px;color:var(--ink);padding-left:22px}
.bullets li::before{content:"";position:absolute;left:2px;top:5px;width:7px;height:7px;border-radius:50%;background:var(--crimson)}
/* testimonials */
.testi{top:2586px;height:462px;background:linear-gradient(110deg,#a53cf2 0%,#7aa8ee 28%,#c59ee6 48%,#f26a8c 70%,#c535e6 100%)}
.review{position:absolute;top:2705px;width:307px;height:214px;background:var(--white);border-radius:4px;padding:20px 20px}
.stars{color:var(--star);font-size:14px;letter-spacing:2px}
.review .date{font-size:10px;color:var(--muted);margin:6px 0 12px}
.review p{font-size:10.5px;line-height:17px;color:var(--ink)}
.review .qm{position:absolute;right:14px;top:6px;font:800 60px/1 'Montserrat',sans-serif;color:#e9e2ee}
.who{position:absolute;left:20px;bottom:16px;display:flex;align-items:center;gap:10px;font-size:11px}
.who .av{width:30px;height:30px;border-radius:50%;background:linear-gradient(135deg,#c9d1e4,#8f9ab5)}
.who b{font-weight:700;color:var(--navy)}
.who small{color:var(--muted);font-size:10px}
/* success */
.success{top:3048px;height:785px;background:var(--white)}
.story{position:absolute;left:182px;top:142px;width:834px;height:426px;background:#e4f1fa}
.story blockquote{position:absolute;left:43px;top:80px;width:370px;font:500 21px/29px 'Lato',sans-serif;color:var(--navy)}
.circle-btn{position:absolute;width:30px;height:30px;border-radius:50%;border:1.5px solid var(--navy);display:flex;align-items:center;justify-content:center}
/* cta */
.cta{position:absolute;left:123px;top:3690px;width:954px;height:212px;border-radius:14px;background:linear-gradient(100deg,#b83ae8 0%,#f0508a 45%,#c43ae2 75%,#7a34f0 100%);z-index:2;text-align:center}
.cta h2{margin-top:58px;font-size:30px;font-weight:600;color:var(--white)}
.cta p{font-size:10.5px;color:var(--white);margin-top:8px}
/* footer */
.footer{top:3833px;height:395px;background:var(--navy)}
.footer .col-h{position:absolute;font:600 14px 'Montserrat',sans-serif;color:var(--white)}
.footer .lnk{position:absolute;font-size:11px;color:#dfe3ee}
.f-ico{position:absolute;width:26px;height:26px;border-radius:50%;background:var(--white);display:flex;align-items:center;justify-content:center}
</style>
</head>
<body>

<!-- HERO -->
<section class="hero">
  <div class="brand abs" style="left:120px;top:10px"><span class="mark"></span>CORVELL SOCIAL</div>
  <nav class="nav">
    <a class="active" style="left:368px">Home</a>
    <a style="left:421px">About Us ▾</a>
    <a style="left:501px">Services ▾</a>
    <a style="left:576px">Portfolio</a>
    <a style="left:641px">Blog</a>
    <a style="left:684px">Contact Us</a>
  </nav>
  <svg class="abs" style="left:878px;top:38px" width="16" height="16" viewBox="0 0 16 16"><circle cx="6.5" cy="6.5" r="5" fill="none" stroke="#0f1c3d" stroke-width="2"/><line x1="10" y1="10" x2="15" y2="15" stroke="#0f1c3d" stroke-width="2"/></svg>
  <div class="btn btn-dark" style="left:903px;top:32px;width:175px;height:28px;padding-left:14px"><span>Get a Free Social Audit</span><span class="arrow" style="width:20px;height:20px"><svg width="10" height="10" viewBox="0 0 10 10"><path d="M2 8L8 2M3 2h5v5" stroke="#0f1c3d" stroke-width="1.6" fill="none"/></svg></span></div>

  <div class="pill abs" style="left:121px;top:187px;width:193px;height:23px">Welcome to Corvell Social</div>
  <h1>Built by a Creator.<br>Designed to Grow<br>Your Brand.</h1>
  <p class="abs" style="left:121px;top:386px;font-size:11px;color:var(--navy)">We do what we know works — because we do it every day.</p>
  <div class="btn btn-light" style="left:121px;top:416px;width:162px;height:36px"><span>Book a Discovery Call</span><span class="arrow"><svg width="10" height="10" viewBox="0 0 10 10"><path d="M2 8L8 2M3 2h5v5" stroke="#fff" stroke-width="1.6" fill="none"/></svg></span></div>

  <svg class="abs" style="left:610px;top:70px" width="520" height="520" viewBox="0 0 520 520"><circle cx="260" cy="260" r="250" fill="none" stroke="#ffffff" stroke-opacity=".5" stroke-dasharray="3 5"/><circle cx="260" cy="260" r="200" fill="none" stroke="#ffffff" stroke-opacity=".35"/></svg>
  <div class="photo" role="img" aria-label="Smiling woman in a grey blazer looking at her phone" style="left:690px;top:110px;width:380px;height:530px;border-radius:190px 190px 0 0;background:linear-gradient(180deg,#c9b3b0 0%,#a59fa6 45%,#8a8e9c 100%)"></div>
  <div class="dot" role="img" aria-label="Live streaming creator avatar" style="left:598px;top:186px;width:58px;height:58px;border:3px solid #f5b14a;background:linear-gradient(135deg,#f6d7c8,#e7b7a6)"></div>
  <span class="abs" style="left:610px;top:236px;background:#e8324a;color:#fff;font:700 9px 'Montserrat',sans-serif;padding:2px 6px;border-radius:6px">LIVE</span>
  <svg class="abs" style="left:640px;top:255px" width="70" height="70" viewBox="0 0 70 70"><path d="M8 4c-6 20 20 22 14 36-4 8-14 2-8-6s30 10 44 22" stroke="#0f1c3d" stroke-width="2" fill="none"/><path d="M54 50l6 6-8 2" stroke="#0f1c3d" stroke-width="2" fill="none"/></svg>
  <div class="dot" style="left:1000px;top:139px;width:32px;height:32px;background:#fff;box-shadow:0 4px 10px rgba(0,0,0,.15)"></div>
  <div class="dot" style="left:1095px;top:289px;width:38px;height:38px;background:#fff;box-shadow:0 4px 10px rgba(0,0,0,.15)"></div>

  <div class="card" style="left:560px;top:390px;width:170px;height:135px;padding:22px 0 0 14px">
    <ul class="checks">
      <li><span class="tick"><svg width="7" height="7" viewBox="0 0 8 8"><path d="M1 4l2 2 4-4" stroke="#fff" stroke-width="1.5" fill="none"/></svg></span>Snapgram Management</li>
      <li><span class="tick"><svg width="7" height="7" viewBox="0 0 8 8"><path d="M1 4l2 2 4-4" stroke="#fff" stroke-width="1.5" fill="none"/></svg></span>ClipTok Management</li>
      <li><span class="tick"><svg width="7" height="7" viewBox="0 0 8 8"><path d="M1 4l2 2 4-4" stroke="#fff" stroke-width="1.5" fill="none"/></svg></span>Social Media Strategy</li>
      <li><span class="tick"><svg width="7" height="7" viewBox="0 0 8 8"><path d="M1 4l2 2 4-4" stroke="#fff" stroke-width="1.5" fill="none"/></svg></span>Content Creation</li>
    </ul>
  </div>
  <div class="card" style="left:921px;top:309px;width:126px;height:42px;text-align:center;padding-top:6px">
    <div class="stars" style="font-size:10px">★★★★★</div>
    <div style="font:600 10px 'Montserrat',sans-serif;color:var(--navy)">Good Services</div>
  </div>
  <div class="card" style="left:922px;top:400px;width:156px;height:114px;padding:20px 12px">
    <div style="display:flex">
      <span class="dot" style="position:static;width:24px;height:24px;background:#e6a989;border:2px solid #fff"></span>
      <span class="dot" style="position:static;width:24px;height:24px;background:#d38aa0;border:2px solid #fff;margin-left:-6px"></span>
      <span class="dot" style="position:static;width:24px;height:24px;background:#1d2233;border:2px solid #fff;margin-left:-6px"></span>
      <span class="dot" style="position:static;width:24px;height:24px;background:#e04b8a;border:2px solid #fff;margin-left:-6px"></span>
    </div>
    <div style="display:flex;justify-content:space-between;font-size:8px;color:var(--navy);margin-top:22px"><span>Secure Sending</span><span>60%</span></div>
    <div style="height:3px;background:#dde3f2;border-radius:2px;margin-top:4px"><div style="width:60%;height:3px;background:var(--blue);border-radius:2px"></div></div>
  </div>
</section>

<!-- ABOUT -->
<section class="about">
  <div class="side-word" style="top:0">CORVELL SOCIAL</div>
  <div class="photo" role="img" aria-label="Smiling woman holding a phone surrounded by floating social app bubbles" style="left:118px;top:52px;width:374px;height:374px;border-radius:50%;background:linear-gradient(150deg,#f3ece8 0%,#e9dbd6 50%,#cdd9ee 100%);box-shadow:inset 0 0 0 5px #9b1f45"></div>
  <div class="dot" style="left:195px;top:22px;width:62px;height:62px;background:#3d8ef0;border-radius:16px;transform:rotate(-14deg)"></div>
  <div class="dot" style="left:430px;top:62px;width:34px;height:34px;background:#f0609a;border-radius:9px"></div>
  <div class="dot" style="left:122px;top:132px;width:36px;height:36px;background:#e8324a;border-radius:9px"></div>
  <div class="dot" style="left:82px;top:248px;width:30px;height:30px;background:#43c765;border-radius:8px"></div>
  <div class="dot" style="left:152px;top:390px;width:46px;height:46px;background:#43c765;border-radius:12px"></div>
  <div class="dot" style="left:482px;top:198px;width:56px;height:56px;background:#2f6fe0;border-radius:14px"></div>
  <div class="dot" style="left:520px;top:328px;width:54px;height:54px;background:#2a74d4;border-radius:14px"></div>
  <div class="logo-disc" style="left:346px;top:323px;width:180px;height:180px">
    <div class="brand"><span class="mark"></span>CORVELL SOCIAL</div>
  </div>

  <div class="label abs" style="left:609px;top:122px">About Us Corvell Social</div>
  <h2 class="abs" style="left:609px;top:144px;font-size:31px;line-height:36px;font-weight:600;color:var(--navy)">Denver's Expert Social<br>Media Management</h2>
  <p class="abs" style="left:609px;top:228px;width:468px;font-size:10.5px;line-height:18.5px;color:var(--muted)">Imagine your company's Snapgram and ClipTok alive with engagement, capturing new audiences, and consistently driving measurable results. This is the elevated standard at Corvell Social, your dedicated social media management partner. Founded by an influencer and content creator, Corvell Social brings an insider's understanding to crafting strategic narratives, creating visually stunning content, and leveraging the latest trends to catapult your online presence. Consider us your dedicated growth team right here in Denver, freeing you to concentrate on what you do best. Ready to elevate your brand's impact through truly strategic social media? Corvell Social: Elevating Social That Drives Results.</p>
  <div class="btn btn-dark" style="left:609px;top:398px;width:125px;height:37px"><span>Learn More</span><span class="arrow"><svg width="10" height="10" viewBox="0 0 10 10"><path d="M2 8L8 2M3 2h5v5" stroke="#0f1c3d" stroke-width="1.6" fill="none"/></svg></span></div>
</section>

<!-- SERVICES -->
<section class="services">
  <div class="label center abs" style="left:545px;top:54px">Services</div>
  <h2 class="abs" style="left:0;width:1200px;text-align:center;top:72px;font-size:30px;font-weight:600;color:var(--navy)">What We Do</h2>

  <div class="abs" style="left:472px;top:138px;width:290px;height:230px;background:var(--navy);transform:rotate(4deg)"></div>
  <div class="svc" style="left:123px;top:147px"><div class="ico"><span></span></div><h3>Snapgram Management</h3><p>We handle everything — content planning, posting, engagement, and DMs. You stay focused on your business while we grow your brand online.</p><div class="more">Learn More →</div></div>
  <div class="svc feature" style="left:448px;top:147px"><div class="ico" style="background:#fff"><span></span></div><h3>ClipTok Management</h3><p>From Reels to short clips, we create dynamic, trend-aware videos that actually get views, saves, and shares.</p><div class="more">Learn More →</div></div>
  <div class="svc" style="left:773px;top:147px"><div class="ico"><span></span></div><h3>Social Media Strategy</h3><p style="color:#8a6fd6">We build custom growth plans using data-backed methods and real influencer insights. No fluff — just results.</p><div class="more">Learn More →</div></div>
  <div class="svc" style="left:123px;top:413px"><div class="ico"><span></span></div><h3>Content Creation</h3><p>Hook your audience and ride the algorithm with expertly crafted captions and targeted hashtags that get seen.</p><div class="more">Learn More →</div></div>
  <div class="svc" style="left:448px;top:413px"><div class="ico"><span></span></div><h3>Community Management</h3><p>Get featured. Get shared. We connect your brand with local and national influencers who align with your message.</p><div class="more">Learn More →</div></div>
  <div class="svc" style="left:773px;top:413px"><div class="ico"><span></span></div><h3>Paid Social Advertising</h3><p>Stay in the loop with monthly insights, performance reports, and strategy adjustments to keep your momentum strong.</p><div class="more">Learn More →</div></div>

  <div class="btn btn-dark" style="left:537px;top:686px;width:126px;height:39px"><span>Learn More</span><span class="arrow"><svg width="10" height="10" viewBox="0 0 10 10"><path d="M2 8L8 2M3 2h5v5" stroke="#0f1c3d" stroke-width="1.6" fill="none"/></svg></span></div>
</section>

<!-- WHY -->
<section class="why">
  <div class="side-word" style="top:0">CORVELL SOCIAL</div>
  <h2 class="abs" style="left:121px;top:168px;font-size:30px;font-weight:600;color:var(--navy)">Why Choose Corvell Social?</h2>
  <ul class="bullets">
    <li style="top:218px">Expertise in Snapgram and ClipTok</li>
    <li style="top:249px">Founder's influencer background providing unique insights.</li>
    <li style="top:281px">Strategic and results-driven approach.</li>
    <li style="top:313px">Local Denver focus.</li>
    <li style="top:345px">Personalized service.</li>
  </ul>
  <div class="btn btn-dark" style="left:121px;top:386px;width:126px;height:37px"><span>Learn More</span><span class="arrow"><svg width="10" height="10" viewBox="0 0 10 10"><path d="M2 8L8 2M3 2h5v5" stroke="#0f1c3d" stroke-width="1.6" fill="none"/></svg></span></div>

  <div class="photo" role="img" aria-label="Woman with glasses using a tablet beside floating notification icons" style="left:648px;top:28px;width:428px;height:456px;border-radius:50%;background:linear-gradient(150deg,#e9e4df 0%,#d6c7a8 55%,#b89a5c 100%);box-shadow:inset 0 0 0 6px #9b1f45"></div>
  <div class="dot" style="left:718px;top:42px;width:60px;height:54px;background:#e8324a;border-radius:12px"></div>
  <div class="dot" style="left:733px;top:126px;width:44px;height:40px;background:#3fb0e8;border-radius:10px"></div>
  <div class="dot" style="left:732px;top:188px;width:50px;height:46px;background:#e8324a;border-radius:10px"></div>
  <div class="dot" style="left:800px;top:86px;width:36px;height:34px;background:#e8324a;border-radius:8px"></div>
  <div class="dot" style="left:800px;top:145px;width:44px;height:40px;background:#3fb0e8;border-radius:10px"></div>
  <div class="logo-disc" style="left:618px;top:312px;width:196px;height:196px">
    <div class="brand"><span class="mark"></span>CORVELL SOCIAL</div>
  </div>
</section>

<!-- TESTIMONIALS -->
<section class="testi">
  <h2 class="abs" style="left:0;width:1200px;text-align:center;top:52px;font-size:31px;font-weight:600;color:var(--navy)">Testimonial</h2>
  <div class="btn btn-dark" style="left:528px;top:362px;width:143px;height:37px"><span>View All Review</span><span class="arrow"><svg width="10" height="10" viewBox="0 0 10 10"><path d="M2 8L8 2M3 2h5v5" stroke="#0f1c3d" stroke-width="1.6" fill="none"/></svg></span></div>
</section>
<article class="review" style="left:121px"><span class="qm">”</span><div class="stars">★★★★★</div><div class="date">Mar 18, 2025</div><p>"We went from barely posting to having a clear, consistent content strategy—and our engagement skyrocketed. Clients even mention our Reels when they book services! Their video strategy is unmatched!"</p><div class="who"><span class="av"></span><span><b>— Renata V.</b> <small>Boutique Owner, Denver</small></span></div></article>
<article class="review" style="left:445px"><span class="qm">”</span><div class="stars">★★★★★</div><div class="date">Feb 6, 2025</div><p>"Their ClipTok videos hit all the right trends without feeling forced or off-brand. We've seen more traffic to our website, and even landed a podcast feature through their content."</p><div class="who"><span class="av"></span><span><b>— Owen K.</b> <small>Gym Owner</small></span></div></article>
<article class="review" style="left:771px"><span class="qm">”</span><div class="stars">★★★★★</div><div class="date">Apr 2, 2025</div><p>"I used to struggle with social media and wasted so much time. Now, I just approve content and focus on running my business. It's stress-free and effective. Corvell Social took over our SG and made it shine!"</p><div class="who"><span class="av"></span><span><b>— Clara P.</b> <small>Realtor</small></span></div></article>

<!-- SUCCESS STORIES -->
<section class="success">
  <h2 class="abs" style="left:0;width:1200px;text-align:center;top:50px;font-size:31px;font-weight:600;color:var(--navy)">Client Success Stories</h2>
  <p class="abs" style="left:0;width:1200px;text-align:center;top:94px;font-size:11px;color:var(--muted)">Led by a creator. Backed by strategy. Built for growth.</p>
  <div class="story">
    <blockquote>“Our SG was dead before Corvell Social. Now, we're booked out every week from Reels alone. I stopped stressing over content. Now I just approve, post, &amp; close new clients. I stopped stressing over content. ”</blockquote>
    <div class="stars abs" style="left:43px;top:267px;font-size:12px">★★★★★</div>
    <div class="abs" style="left:43px;top:286px;font-size:13px;color:var(--navy)"><b>Tamsin R.,</b> <span style="font-size:11px;color:var(--muted)">Beauty Studio Owner</span></div>
    <div class="circle-btn" style="left:43px;top:322px"><svg width="12" height="10" viewBox="0 0 12 10"><path d="M11 5H1M5 1L1 5l4 4" stroke="#0f1c3d" stroke-width="1.5" fill="none"/></svg></div>
    <div class="circle-btn" style="left:82px;top:322px"><svg width="12" height="10" viewBox="0 0 12 10"><path d="M1 5h10M7 1l4 4-4 4" stroke="#0f1c3d" stroke-width="1.5" fill="none"/></svg></div>
    <div class="photo" role="img" aria-label="Smiling businessman in a dark suit giving a thumbs up" style="left:440px;top:52px;width:342px;height:320px;background:linear-gradient(160deg,#cfe8ec 0%,#9fcfd7 55%,#2a3140 100%)"></div>
  </div>
</section>

<!-- CTA -->
<div class="cta">
  <h2>Ready to Grow Your Social?</h2>
  <p>Let's build content that connects, converts, and keeps your audience coming back.</p>
  <div class="btn btn-light" style="left:401px;top:126px;width:148px;height:35px"><span>Let's Get Started</span><span class="arrow"><svg width="10" height="10" viewBox="0 0 10 10"><path d="M2 8L8 2M3 2h5v5" stroke="#fff" stroke-width="1.6" fill="none"/></svg></span></div>
</div>

<!-- FOOTER -->
<footer>
<section class="footer">
  <div class="brand abs" style="left:120px;top:98px;align-items:flex-start"><span class="mark"></span>CORVELL SOCIAL</div>
  <p class="abs" style="left:120px;top:182px;width:180px;font-size:10.5px;line-height:18px;color:#dfe3ee">Denver's influencer-led social media agency. We create content that connects &amp; grows your brand.</p>

  <div class="col-h" style="left:341px;top:133px">Company</div>
  <span class="lnk" style="left:341px;top:182px">Services</span>
  <span class="lnk" style="left:341px;top:209px">Portfolio</span>
  <span class="lnk" style="left:341px;top:236px">Blog</span>
  <span class="lnk" style="left:341px;top:263px">About Us</span>
  <span class="lnk" style="left:341px;top:290px">Contact</span>

  <div class="col-h" style="left:471px;top:133px">Contact Us</div>
  <span class="f-ico" style="left:471px;top:180px"><svg width="10" height="13" viewBox="0 0 10 13"><path d="M5 12S1 7.5 1 5a4 4 0 018 0c0 2.5-4 7-4 7z" fill="#0f1c3d"/><circle cx="5" cy="5" r="1.5" fill="#fff"/></svg></span>
  <span class="lnk" style="left:516px;top:182px;width:150px;line-height:17px">Northgate Studio, 14 Larchmere Row, Ashby Vale AV4 2QT</span>
  <span class="f-ico" style="left:471px;top:232px"><svg width="12" height="12" viewBox="0 0 12 12"><path d="M3 1l2 3-1.5 1.2a7 7 0 003.3 3.3L8 7l3 2-1 2.2C5 11 1 7 0.8 2z" fill="#0f1c3d"/></svg></span>
  <span class="lnk" style="left:516px;top:239px">0100 555 0147</span>
  <span class="f-ico" style="left:471px;top:278px"><svg width="12" height="12" viewBox="0 0 12 12"><path d="M11 1L1 5.5l4 1.5 1.5 4z" fill="#0f1c3d"/></svg></span>
  <span class="lnk" style="left:516px;top:285px">hello@corvellsocial.example</span>

  <div class="col-h" style="left:708px;top:133px">Community</div>
  <span class="f-ico" style="left:708px;top:179px"></span><span class="lnk" style="left:752px;top:185px">ClipTok</span>
  <span class="f-ico" style="left:708px;top:224px"></span><span class="lnk" style="left:752px;top:230px">Snapgram</span>
  <span class="f-ico" style="left:708px;top:268px"></span><span class="lnk" style="left:752px;top:274px">WorkLink</span>

  <div class="col-h" style="left:875px;top:135px">Newsletter</div>
  <span class="lnk" style="left:875px;top:182px">Subscribe to our newsletter</span>
  <div class="abs" style="left:875px;top:209px;width:202px;height:42px;border:1px solid #b8c0d6;border-radius:22px;font-size:10px;color:#dfe3ee;padding:14px 22px">Enter email...</div>
  <div class="btn btn-light" style="left:875px;top:267px;width:127px;height:37px"><span>Subscribe</span><span class="arrow"><svg width="10" height="10" viewBox="0 0 10 10"><path d="M2 8L8 2M3 2h5v5" stroke="#fff" stroke-width="1.6" fill="none"/></svg></span></div>

  <div class="abs" style="left:0;top:345px;width:1200px;height:1px;background:#2a3760"></div>
  <p class="abs" style="left:0;width:1200px;text-align:center;top:367px;font-size:10.5px;color:#dfe3ee;word-spacing:2px">© 2025 Corvell Social - All rights reserved &nbsp;&nbsp; | &nbsp;&nbsp; Privacy Policy &nbsp;&nbsp; | &nbsp;&nbsp; Terms &amp; Conditions</p>
</section>
</footer>

</body>
</html>
```